依頼詳細
現サイト http://www.kozanso-hp.jp/

今回のリニューアルでは基調色を「緑以外」というご希望です。
素材は下記からダウンロードしていただけます。
※容量が大きいです。施設パンフなどに使ったものを一切合切入れてあります。

自由な発想でデザインしてみてください。
シンプル系もありだと思います。
サイトURL
http://www.kozanso-hp.jp/
ページ数
1ページ
希望イメージ
シンプル 複雑
単色 カラフル
暗い 明るい
日常 高級
遊び心 厳粛
未来的 伝統的
女性的 男性的
希望する色
赤系、水色系、黄・オレンジ系
納品ファイル
• フォトショップ形式 (.psd)
• PNG形式 (.png)
補足説明
サイトマップを添付致します。
★タイトなスケジュールで申し訳ありませんが、ぜひご提案くださいませ。
よろしくお願い致します!
素材のダウンロード先を記入し忘れておりました。申し訳ありません。
https://dl3.fomvault.jp/get/9b2d17ac53e04f6ab81c92d7e4f0a6b3.html
(パスワード: peWoxiMt)
サイトマップの添付を追加致しました。
選定確約という機能があることを知りました。チェックをいれましたので必ず当選者様を選定致します。
■ 選んだ理由

tokinekaho様
お世話になります。今回のご提案をクライアント様に気に入っていただきました。修正なしでこのままでOKでございます。
シンプル系がやはりクライアント様が選んだ一番の理由だったと思います。
すばらしいです。

■ 提案者全員のお礼・コメント

弊社判断で当選を決定できなかったのですが、先方クライアント様との打ち合わせで、「おそらくこれが一番気に入られるかな」という印象でした。
昨日、プリントアウトしてプリンターの加減も含めた中で、当選決定となりました。やはりディレクションの重要さとそれをクラウドソーシングに伝える難しさや良さも同時に感じました。
今回は本当にありがとうございます。
株式会社ケミノ 杉浦

```html
<!DOCTYPE html>
<html lang="ja">
<head>
<meta charset="utf-8">
<title>特別養護老人ホーム 香山荘</title>
<link rel="stylesheet" href="https://fonts.googleapis.com/css2?family=Noto+Sans+JP:wght@400;500;700&family=Noto+Serif+JP:wght@400;500&display=swap">
<style>
:root{
  --accent:#d9532b;
  --ink:#333;
  --muted:#777;
  --brown:#8a6a52;
  --brown-dark:#6d513e;
  --tagline:#9a7a5c;
  --line:#d8cfc5;
  --bg:#fff;
}
*{margin:0;padding:0;box-sizing:border-box}
html,body{width:691px;height:1200px;overflow:hidden;background:var(--bg)}
body{font-family:"Noto Sans JP",sans-serif;color:var(--ink);position:relative}
.site-header{position:absolute;left:0;top:0;width:691px;height:125px}
.org-name{position:absolute;left:30px;top:14px;font-size:17px;color:var(--accent);font-weight:500}
.facility-name{position:absolute;left:66px;top:46px;font-size:20px;color:var(--ink);font-weight:500;letter-spacing:1px}
.facility-name .brand{font-size:22px;margin-left:8px}
.contact{position:absolute;left:462px;top:24px}
.contact .tel{font-size:17px;color:var(--ink);display:flex;align-items:center;gap:5px}
.contact .addr{font-size:8px;color:var(--muted);line-height:1.4;margin-top:3px}
.request{position:absolute;left:600px;top:28px;width:72px;height:52px;border:2px solid var(--accent);color:var(--accent);font-size:10px;line-height:1.35;text-align:center;padding-top:10px}
.global-nav{position:absolute;left:0;top:90px;width:691px;display:flex;justify-content:center;font-size:14px}
.global-nav a{color:var(--ink);text-decoration:none;padding:0 9px;border-left:1px solid #999;line-height:1}
.global-nav a:first-child{border-left:none}
.hero{position:absolute;left:10px;top:132px;width:671px;height:432px;background:linear-gradient(135deg,#5e7a3c 0%,#9bb86a 35%,#dfe6c8 60%,#7f9a55 100%)}
.tagline{position:absolute;left:0;top:574px;width:691px;text-align:center;font-family:"Noto Serif JP",serif;color:var(--tagline);font-size:15px;line-height:1.6}
.section-title{font-size:15px;color:var(--brown-dark);font-weight:500;border-bottom:1px solid var(--line);padding-bottom:3px;height:26px;line-height:22px}
.services{position:absolute;left:30px;top:652px;width:631px}
.service-grid{position:relative;height:190px}
.service{position:absolute;width:116px;text-align:center;font-size:9px;line-height:12px;color:var(--ink);white-space:nowrap}
.service .thumb{width:116px;height:60px;margin-bottom:3px}
.news{position:absolute;top:870px;width:300px}
.news.left{left:30px}
.news.right{left:357px}
.news ul{list-style:none;margin-top:4px}
.news li{font-size:12px;line-height:1;padding:8px 0;height:30px;border-bottom:1px dotted var(--line);display:flex;gap:8px;white-space:nowrap;overflow:hidden}
.news .date{color:var(--accent)}
.news .date::before{content:"▸ ";}
.site-footer{position:absolute;left:0;top:1100px;width:691px;height:100px;background:var(--brown);color:#fff;text-align:center}
.footer-brand{display:inline-flex;align-items:center;gap:14px;margin-top:14px}
.footer-brand .name{font-size:24px;font-weight:500;letter-spacing:3px;border:1px solid #fff;padding:2px 10px}
.footer-brand .info{font-size:9px;text-align:left;line-height:1.5}
.copyright{font-size:9px;margin-top:10px;color:#eadfd4}
</style>
</head>
<body>
<header class="site-header">
  <p class="org-name">社会福祉法人 光和会</p>
  <p class="facility-name">特別養護老人ホーム<span class="brand">香山荘</span></p>
  <div class="contact">
    <p class="tel"><svg width="14" height="14" viewBox="0 0 24 24"><path d="M6.6 10.8a15 15 0 0 0 6.6 6.6l2.2-2.2c.3-.3.7-.4 1-.2 1.1.4 2.3.6 3.6.6.6 0 1 .4 1 1V20c0 .6-.4 1-1 1A17 17 0 0 1 3 4c0-.6.4-1 1-1h3.5c.6 0 1 .4 1 1 0 1.3.2 2.5.6 3.6.1.3 0 .7-.2 1z" fill="#d9532b"/></svg>0745-00-1234</p>
    <p class="addr">FAX 0745-00-1235<br>〒633-0000 奈良県宇陀市1-2-3</p>
  </div>
  <div class="request">資料請求<br>お問い合わせ</div>
  <nav class="global-nav">
    <a href="#">トップ</a><a href="#">特養施設概要</a><a href="#">短期施設案内</a><a href="#">事業内容</a><a href="#">お問い合わせ</a><a href="#">よくある質問</a>
  </nav>
</header>

<div class="hero" role="img" aria-label="緑の木々の中で車椅子を押す職員の写真"></div>

<p class="tagline">緑豊か、清浄な空気と四季折々の自然に恵まれ、<br>静かな環境の中、特別養護老人ホーム<br>を中心に様々なサービスを提供しています。</p>

<section class="services">
  <h2 class="section-title">事業内容</h2>
  <div class="service-grid">
    <div class="service" style="left:74px;top:10px"><div class="thumb" role="img" aria-label="施設の外観写真" style="background:linear-gradient(#9ec3e6,#c9d6b8 55%,#8a9a6a)"></div>特別養護老人ホーム</div>
    <div class="service" style="left:262px;top:10px"><div class="thumb" role="img" aria-label="居室の写真" style="background:linear-gradient(#e8dcc4,#c9ad85)"></div>ショートステイ</div>
    <div class="service" style="left:446px;top:10px"><div class="thumb" role="img" aria-label="食堂の写真" style="background:linear-gradient(#e3d6bf,#b89a72)"></div>デイサービス</div>
    <div class="service" style="left:74px;top:96px"><div class="thumb" role="img" aria-label="介護の様子の写真" style="background:linear-gradient(#d4d4d4,#9a9a9a)"></div>居宅介護支援センター</div>
    <div class="service" style="left:262px;top:96px"><div class="thumb" role="img" aria-label="山並みの風景写真" style="background:linear-gradient(#9cc3e8,#7fa46a 60%,#4f6e3a)"></div>交通アクセス</div>
  </div>
</section>

<section class="news left">
  <h2 class="section-title">お知らせ</h2>
  <ul>
    <li><span class="date">2016/08/18</span>新しいパンフレットができ…</li>
    <li><span class="date">2016/07/25</span>リノベーション完了です。</li>
    <li><span class="date">2016/07/25</span>設置前の説明をしました…</li>
    <li><span class="date">2016/06/20</span>平成２７年度決算事業報告…</li>
    <li><span class="date">2016/06/20</span>もうすぐリニューアル工事が…</li>
  </ul>
</section>

<section class="news right">
  <h2 class="section-title">採用情報</h2>
  <ul>
    <li><span class="date">2015/10/01</span>介護の仕事って誰でもできる？</li>
    <li><span class="date">2015/06/16</span>介護の仕事・・・</li>
    <li><span class="date">2014/11/19</span>平成２６年の振りかえりです…</li>
    <li><span class="date">2013/04/01</span>介護職員さん、看護職員さん…</li>
    <li><span class="date">2012/02/24</span>看護師さん、介護職員募集中…</li>
  </ul>
</section>

<footer class="site-footer">
  <div class="footer-brand">
    <span class="name">香山荘</span>
    <p class="info">特別養護老人ホーム 香山荘<br>〒633-0000 奈良県宇陀市1-2-3<br>TEL 0745-00-1234</p>
  </div>
  <p class="copyright">Copyright © kozanso. All Rights Reserved.</p>
</footer>
</body>
</html>
```